Menu Design Project for new restauranct concept

Design menu for new restaurant concept called Juniper's Burgers & Dogs. Logo is attached.

Industry/Entity Type

Restaurant

Requirements
Must have
• Menu items and pricing:

Burgers
Snack Burger $3.49
Snack Cheeseburger $3.99
Juniper's signature Burger $4.99
Juniper's signature Cheeseburger $5.49
Burger toppings: bacon, lettuce, tomato, onion, pickle, grilled onions, grilled mushrooms, grilled green peppers, jalapeƱo peppers.

Dogs
Hot Dog $2.99
Bacon Cheese Hot Dog $3.99
Slaw Dog $3.99
Kraut Dog $3.49
Chili Dog $3.99 with or with out cheese
Hot dogs are 100% beef

Other
Grilled Chicken Sandwich $5.99
Grilled Chicken Sandwich with cheese $6.49
(Same toppings as burgers)

French Fries $1.99

Loaded Potatos
The Plain Tater: $4.99 choose from: butter, sour cream, cheese, chives
The Garden Tater: $5.99 choose from: the Basic plus, broccoli & cheese, grilled mushrooms, onions, & peppers
The Carver Tater: $6.99 choose from the Basic/Veggie plus: grilled chicken, chili, Philly cheesesteak, pulled pork.

Drinks
32oz. Drink $1.88
20oz. Drink $1.69

attached logo.
Nice to have
• love to incorporate the woodgrain backgound. It makes the logo look most like a cattle brand, which we like.

```html
<!DOCTYPE html>
<html lang="en">
<head>
<meta charset="utf-8">
<title>Juniper's Burgers &amp; Dogs — Menu</title>
<link rel="stylesheet" href="https://fonts.googleapis.com/css2?family=Fira+Sans+Condensed:ital,wght@0,400;0,600;0,700;1,400&family=Oswald:wght@700&display=swap">
<style>
  :root {
    --paper: #a59479;
    --ink: #2b251e;
    --wood-dark: #5e4a42;
    --wood-mid: #7a655c;
    --wood-light: #9c968c;
    --wood-pale: #b5b0a6;
    --ghost: rgba(120, 104, 82, 0.45);
  }
  * { margin: 0; padding: 0; box-sizing: border-box; }
  html, body { width: 927px; height: 1200px; overflow: hidden; }
  body {
    position: relative;
    background: var(--paper);
    color: var(--ink);
    font-family: "Fira Sans Condensed", "Arial Narrow", sans-serif;
  }
  .wood-band {
    position: absolute; left: 0; top: 0; width: 927px; height: 235px;
    background: linear-gradient(90deg, var(--wood-mid), var(--wood-dark) 30%, var(--wood-mid) 55%, var(--wood-dark) 80%, var(--wood-mid));
  }
  .brand-panel {
    position: absolute; left: 73px; top: 0; width: 321px; height: 261px;
    background: linear-gradient(90deg, var(--wood-light), var(--wood-pale) 40%, var(--wood-light) 70%, var(--wood-pale));
    display: flex; flex-direction: column; align-items: center; justify-content: center;
  }
  .brand-name {
    font-weight: 700; color: #2a2622; text-align: center; line-height: 1.05;
    font-size: 44px; text-transform: uppercase;
  }
  .brand-name span { display: block; font-size: 28px; }
  .ghost-circle {
    position: absolute; left: 122px; top: 303px; width: 666px; height: 666px;
    border: 22px solid var(--ghost); border-radius: 50%;
  }
  .ghost-words {
    position: absolute; left: 0; width: 927px; top: 1070px; text-align: center;
    font-family: "Oswald", "Arial Narrow", sans-serif; font-weight: 700;
    font-size: 92px; letter-spacing: 3px; color: var(--ghost); line-height: 1;
  }
  .section { position: absolute; }
  .section h2 { font-size: 23px; font-weight: 700; margin-bottom: 14px; }
  .section h2 em { font-size: 15px; font-weight: 400; margin-left: 22px; }
  .item { font-size: 18px; line-height: 27px; }
  .price { font-weight: 700; margin-left: 8px; }
  .note { font-style: italic; font-size: 16px; line-height: 23px; }
  .item .note { margin-left: 8px; }
  .choice { font-style: italic; font-size: 16px; line-height: 27px; padding-left: 14px; margin-bottom: 2px; }
  .burgers { left: 473px; top: 268px; width: 400px; }
  .burgers .note { margin-top: 12px; }
  .dogs { left: 106px; top: 432px; }
  .potatoes { left: 473px; top: 621px; width: 400px; }
  .potatoes .item { line-height: 28px; }
  .other { left: 106px; top: 836px; }
  .other .indent { font-style: italic; font-size: 15px; line-height: 27px; padding-left: 14px; }
</style>
</head>
<body>
  <div class="wood-band" role="img" aria-label="Weathered woodgrain planks"></div>
  <div class="brand-panel">
    <div class="brand-name">Juniper's<span>Burgers &amp; Dogs</span></div>
  </div>
  <div class="ghost-circle"></div>

  <section class="section burgers">
    <h2>Burgers</h2>
    <div class="item">Snack Burger<span class="price">$3.49</span></div>
    <div class="item">Snack Cheeseburger<span class="price">$3.99</span></div>
    <div class="item">Juniper's signature Burger<span class="price">$4.99</span></div>
    <div class="item">Juniper's signature Cheeseburger<span class="price">$5.49</span></div>
    <p class="note">Burger toppings: bacon, lettuce, tomato, onion, pickle, grilled onions, grilled mushrooms, grilled green peppers, jalapeño peppers.</p>
  </section>

  <section class="section dogs">
    <h2>Dogs<em>100% beef</em></h2>
    <div class="item">Hot Dog<span class="price">$2.99</span></div>
    <div class="item">Bacon Cheese Hot Dog<span class="price">$3.99</span></div>
    <div class="item">Slaw Dog<span class="price">$3.99</span></div>
    <div class="item">Kraut Dog<span class="price">$3.49</span></div>
    <div class="item">Chili Dog<span class="price">$3.99</span><span class="note">with or without cheese</span></div>
  </section>

  <section class="section potatoes">
    <h2>Loaded Potatos</h2>
    <div class="item">The Plain Tater<span class="price">$4.99</span></div>
    <p class="choice">Choose from: butter, sour cream, cheese, chives</p>
    <div class="item">The Garden Tater<span class="price">$5.99</span></div>
    <p class="choice">Choose from: the Basic plus, broccoli &amp; cheese, grilled mushrooms, onions, &amp; peppers</p>
    <div class="item">The Carver Tater<span class="price">$6.99</span></div>
    <p class="choice">Choose from the Basic/Veggie plus: grilled chicken, chili, Philly cheesesteak, pulled pork.</p>
  </section>

  <section class="section other">
    <h2>Other</h2>
    <div class="item">Grilled Chicken Sandwich<span class="price">$5.99</span></div>
    <div class="item">Grilled Chicken Sandwich w/ cheese<span class="price">$6.49</span></div>
    <div class="indent">Same toppings as burgers</div>
    <div class="item">French Fries<span class="price">$1.99</span></div>
    <div class="item">32 oz. Drink<span class="price">$1.88</span></div>
    <div class="item">20 oz. Drink<span class="price">$1.69</span></div>
  </section>

  <div class="ghost-words">BURGERS &amp; DOGS</div>
</body>
</html>
```